International oil and gas consultancy business needs a web design

Hello, I need a web design for a new oil and gas auditing consultancy business. My business undertakes contract audit assignments to review past costs of oil and gas operations (see attached Excel file for more details of the businesses services). I need the design to give the impression of a professional consultancy style of business, rather than a retail style of website. Note: this job is for LAYOUT DESIGN ONLY and not coding / development work.
The following are my key design principles:
1. BASIC DESIGN: I am after a simple and static web design. I don't want the pages busy or cluttered with too many images or detail.
2. HORIZONTAL TABS: I require a horizontal set of tabs towards the top of the screens (see Excel file) which remain in the same position on every page.
3. META TAG PLANNING: The design should allow for effective positioning of content so that key meta tag words can easily be built during the technical build stage.
4. NUMBER OF PAGES: The site will eventually have a maximum of 10 pages. Seven of the pages will reside under the tabs. Can you please present your opening submission for the first two page.
5. USE OF MY LOGO: The attached logo (JPEG file) should be used throughout the website. Please don't change the shape and colour.
6. COLOUR SCHEMES: Can you please consider any of the 3 colour schemes below:
A - dark red (to match the logo), light grey and perhaps another of your liking;
B - dark red (to match the logo), light cream and perhaps another of your liking;
C - dark red (to match the logo), white and perhaps another of your liking.
7. WORD CONTENT: I have attached an Excel file which shows the estimated word content for each page.
8. FUTURE USE OF DESIGN: I'm planning on building a Wordpress website. Can you please ensure the layout design supports this application.

Target Market(s)

oil and gas companies (small and large)

Industry/Entity Type

Oil And Gas

Font styles to use
Sans Serif

Requirements
Nice to have
• The KOL logo and business name should ideally be next to each other. Also, the logo and name should be part of the background graphics, not above it.

```html
<!DOCTYPE html>
<html lang="en">
<head>
<meta charset="utf-8">
<title>KOL – Kingsford Operations Ledger</title>
<link href="https://fonts.googleapis.com/css2?family=Arimo:wght@400;700&display=swap" rel="stylesheet">
<style>
:root{
  --red:#8e1a1f;
  --text:#555;
  --dark:#333;
  --line:#c8c8c8;
  --band:#f9f9f9;
  --white:#fff;
  --muted:#888;
}
*{margin:0;padding:0;box-sizing:border-box}
html,body{width:1200px;height:1000px;overflow:hidden}
body{font-family:"Arimo",Arial,sans-serif;background:var(--white);color:var(--text);position:relative}
.top-band{position:absolute;left:0;top:0;width:1200px;height:675px;background:var(--band);border-bottom:1px solid #ececec;box-shadow:0 2px 6px rgba(0,0,0,.04)}
.brand{position:absolute;left:155px;top:36px}
.brand-mark{font-size:50px;font-weight:700;color:var(--red);letter-spacing:4px;line-height:52px}
.brand-name{font-size:15px;color:var(--red);margin-top:4px}
.main-nav{position:absolute;left:509px;top:72px;width:563px;height:35px;border-bottom:1px solid var(--line);display:flex;justify-content:space-between}
.main-nav a{font-size:11px;color:var(--dark);text-decoration:none;text-transform:uppercase;position:relative;height:35px}
.main-nav a.active{color:var(--red)}
.main-nav a.active::after{content:"";position:absolute;left:0;right:0;bottom:-2px;height:3px;background:var(--red)}
.hero{position:absolute;left:155px;top:135px;width:917px;height:373px;background:linear-gradient(135deg,#2b3a55 0%,#c9d4e0 35%,#eef2f6 60%,#e6d3c8 100%);box-shadow:0 -6px 10px -6px rgba(0,0,0,.2)}
.hero-pager{position:absolute;left:565px;top:483px;width:97px;height:32px;background:#f4f4f4;box-shadow:0 2px 4px rgba(0,0,0,.15);display:flex;justify-content:center;align-items:center;gap:5px;padding-bottom:4px}
.hero-pager span{width:9px;height:9px;border-radius:50%;background:#888}
.hero-pager span.current{background:var(--red)}
.intro{position:absolute;left:210px;top:558px;width:806px;text-align:center;font-size:15px;line-height:23.5px;color:var(--text)}
.intro strong{color:var(--red);font-size:17px}
.services{position:absolute;top:748px;left:0;width:1200px}
.service{position:absolute;top:0;width:240px}
.service-icon{position:absolute;left:0;top:2px;width:72px;height:72px;border-radius:50%;background:radial-gradient(circle at 50% 40%,#fff 55%,#ececec 100%);box-shadow:0 4px 5px rgba(0,0,0,.3);display:flex;align-items:center;justify-content:center}
.service-title{position:absolute;left:87px;top:2px;width:152px;font-size:17px;color:var(--dark);font-weight:400;padding-bottom:8px;border-bottom:3px solid var(--line);white-space:nowrap}
.service-title.featured{color:var(--red)}
.service-text{position:absolute;left:88px;top:48px;width:150px;font-size:10.5px;line-height:15px;color:var(--text)}
.site-footer{position:absolute;left:0;top:922px;width:1200px;height:78px;border-top:1px solid #ddd}
.footer-mark{position:absolute;left:157px;top:22px;font-size:22px;font-weight:700;color:#b5b5b5;letter-spacing:2px}
.footer-divider{position:absolute;left:242px;top:24px;width:1px;height:18px;background:var(--line)}
.footer-text{position:absolute;left:259px;top:27px;font-size:9.5px;color:var(--muted)}
.footer-text a{color:var(--muted);text-decoration:none}
</style>
</head>
<body>
<div class="top-band"></div>
<header>
  <div class="brand">
    <div class="brand-mark">KOL</div>
    <div class="brand-name">Kingsford Operations Ledger</div>
  </div>
  <nav class="main-nav">
    <a class="active" href="#">Home</a>
    <a href="#">About Us</a>
    <a href="#">Services</a>
    <a href="#">Our Partners</a>
    <a href="#">Aproach</a>
    <a href="#">Why Choose Us</a>
    <a href="#">Contact Us</a>
  </nav>
</header>

<div class="hero" role="img" aria-label="Photo of business hands reviewing printed financial charts with a pen and tablet"></div>
<div class="hero-pager"><span></span><span class="current"></span><span></span><span></span><span></span></div>

<p class="intro"><strong>Kingsford Operations Ledger</strong> is a Perth (Australia) based firm specialising in providing quality audit services for the oil and gas industry. Our skills and knowledge of oil and gas, along with a deep understanding of business commercial needs, ensures the high quality of our services</p>

<section class="services">
  <div class="service" style="left:153px">
    <div class="service-icon">
      <svg width="32" height="32" viewBox="0 0 32 32"><path d="M6 26 L8 19 L21 6 L26 11 L13 24 Z" fill="#8e1a1f"/><path d="M6 26 L8 19 L13 24 Z" fill="#6e1216"/></svg>
    </div>
    <h3 class="service-title featured">Joint Venture Audits</h3>
    <p class="service-text">Our role in these assignments, is to represent one or more of the 'Non-Operating' partners</p>
  </div>
  <div class="service" style="left:514px">
    <div class="service-icon">
      <svg width="32" height="32" viewBox="0 0 32 32" fill="none" stroke="#999" stroke-width="1.5"><rect x="4" y="6" width="22" height="21"/><rect x="7" y="4" width="21" height="21" fill="#f3f3f3"/><rect x="10" y="8" width="7" height="6"/><path d="M19 9h6M19 12h6M10 17h15M10 20h15M10 23h15"/></svg>
    </div>
    <h3 class="service-title">Contract Audits</h3>
    <p class="service-text">Our role in contract audit assignments, is to represent the Operator and review the records</p>
  </div>
  <div class="service" style="left:832px">
    <div class="service-icon">
      <svg width="34" height="34" viewBox="0 0 34 34"><rect x="5" y="13" width="7" height="16" fill="#c4c4c4"/><rect x="13" y="6" width="7" height="23" fill="#d6d6d6"/><rect x="21" y="11" width="7" height="18" fill="#c4c4c4"/></svg>
    </div>
    <h3 class="service-title">Operations Audits</h3>
    <p class="service-text">Our role in Operational audit assignments, is to target specific areas of an Operators</p>
  </div>
</section>

<footer class="site-footer">
  <div class="footer-mark">KOL</div>
  <div class="footer-divider"></div>
  <p class="footer-text">Copyright All Right Reserved Company Name 2014 &nbsp; <a href="#">Privacy Policy</a> &nbsp;|&nbsp; <a href="#">Terms and Condition</a></p>
</footer>
</body>
</html>
```